Brolvane Co.,Ltd. need business card

Brolvane Company Limited is a facility management company. We provides a total solution services from administration, energy saving, security, safety, food catering to companies.

The logo should be in elegant style with innovative that suited to the upper market
Please see the logo image in the attached file. You can use this Red or Blue or Green checkerboard (color and font should be similar to logo) as the main part of business card (can be an entire of one side of business card) . In another side of card should contain contact details of personnel - here below demo information

Kanyarat Thoengsai
Chief Executive Officer

No.73, Soi 5, Ruam Wongsa Road
Nong Khaem, Bangkok,
10520, Thailand

Tel + 66841537296
Mobile + 66841537296
E-mail: Kanyarat.Thoengsai@brolvane-example.co.th

Target Market(s)

Factory, Hotel and Hospital

Industry/Entity Type

Business

Contact Information for Business Card

Kanyarat Thoengsai
Chief Executive Officer

Nong Khaem, Bangkok,
10520, Thailand

Tel + 66841537296
Mobile + 66841537296

We will change details with the winner designer

Font styles to use
Sans Serif

Requirements
Must have
• In style of red checkerboard and white color

```html
<!DOCTYPE html>
<html lang="en">
<head>
<meta charset="utf-8">
<title>Brolvane Co.,Ltd. — Business Card</title>
<link rel="stylesheet" href="https://fonts.googleapis.com/css2?family=Open+Sans:wght@400;600;700&display=swap">
<style>
  :root {
    --backdrop: #ececec;
    --brand-red: #c8151f;
    --brand-red-deep: #a50f18;
    --paper: #ffffff;
    --ink: #3c3c3c;
    --ink-soft: #7a7a7a;
    --card-shadow: rgba(0, 0, 0, 0.18);
  }
  * { box-sizing: border-box; margin: 0; padding: 0; }
  html, body {
    width: 1200px;
    height: 800px;
    overflow: hidden;
    background: var(--backdrop);
    font-family: "Open Sans", Arial, sans-serif;
  }
  .stage {
    position: relative;
    width: 1200px;
    height: 800px;
  }
  .card {
    position: absolute;
    top: 250px;
    width: 520px;
    height: 300px;
    box-shadow: 0 6px 18px var(--card-shadow);
    overflow: hidden;
  }
  .card--front { left: 60px; }
  .card--back  { left: 620px; background: var(--paper); }

  /* Front */
  .front-field {
    position: absolute;
    inset: 0;
    background: linear-gradient(135deg, var(--brand-red) 0%, var(--brand-red-deep) 100%);
  }
  .brand-name {
    position: absolute;
    inset: 0;
    display: flex;
    align-items: center;
    justify-content: center;
    color: var(--paper);
    font-weight: 400;
    font-size: 50px;
    letter-spacing: 14px;
    padding-left: 14px;
  }

  /* Back */
  .edge-band {
    position: absolute;
    left: 0; top: 0; bottom: 0;
    width: 18px;
    background: var(--brand-red);
  }
  .contact {
    position: absolute;
    left: 52px;
    top: 108px;
    right: 30px;
  }
  .person-name {
    font-size: 23px;
    line-height: 1.1;
    color: var(--brand-red);
    font-weight: 400;
  }
  .person-name .given { font-weight: 700; }
  .person-title {
    font-size: 13px;
    color: var(--ink-soft);
    margin-top: 2px;
  }
  .details {
    margin-top: 18px;
    list-style: none;
  }
  .detail {
    display: flex;
    align-items: flex-start;
    gap: 10px;
    margin-bottom: 10px;
    font-size: 10.5px;
    line-height: 1.35;
    color: var(--ink);
  }
  .detail strong { font-weight: 700; }
  .detail-icon {
    flex: 0 0 16px;
    width: 16px;
    height: 16px;
    margin-top: 1px;
  }
  .detail-text--muted { color: var(--ink-soft); }
</style>
</head>
<body>
<main class="stage">
  <section class="card card--front" aria-label="Business card front">
    <div class="front-field" role="img" aria-label="Red checkerboard pattern background"></div>
    <div class="brand-name">BROLVANE</div>
  </section>

  <section class="card card--back" aria-label="Business card back">
    <div class="edge-band"></div>
    <div class="contact">
      <h1 class="person-name"><span class="given">Kanyarat</span> Thoengsai</h1>
      <p class="person-title">Chief Executive Officer</p>
      <ul class="details">
        <li class="detail">
          <svg class="detail-icon" viewBox="0 0 16 16" aria-hidden="true">
            <rect width="16" height="16" rx="2" fill="var(--brand-red)"/>
            <path d="M3.5 8 L8 4 L12.5 8 M5 7.2 V12 H11 V7.2" fill="none" stroke="#fff" stroke-width="1.3" stroke-linejoin="round"/>
          </svg>
          <span>No.73, <strong>Soi 5</strong>, Ruam Wongsa Road<br>Nong Khaem, <strong>Bangkok,</strong><br>10520, Thailand</span>
        </li>
        <li class="detail">
          <svg class="detail-icon" viewBox="0 0 16 16" aria-hidden="true">
            <rect width="16" height="16" rx="2" fill="var(--brand-red)"/>
            <path d="M5 3.5 L6.8 3.5 L7.5 6 L6.4 7 Q7.3 8.8 9 9.6 L10 8.5 L12.5 9.2 L12.5 11 Q12 12.5 10.5 12.4 Q4 11.5 3.6 5 Q3.6 3.8 5 3.5 Z" fill="#fff"/>
          </svg>
          <span class="detail-text--muted">+ 66841537296<br>+ 66841537296</span>
        </li>
        <li class="detail">
          <svg class="detail-icon" viewBox="0 0 16 16" aria-hidden="true">
            <rect width="16" height="16" rx="2" fill="var(--brand-red)"/>
            <rect x="3.5" y="5" width="9" height="6.5" fill="none" stroke="#fff" stroke-width="1.2"/>
            <path d="M3.5 5 L8 8.6 L12.5 5" fill="none" stroke="#fff" stroke-width="1.2"/>
          </svg>
          <span class="detail-text--muted">Kanyarat.Thoengsai@brolvane-example.co.th</span>
        </li>
      </ul>
    </div>
  </section>
</main>
</body>
</html>
```